Business Card Design Project

I am a Chiropractor that is looking for a new business card.  Our logo was slightly changed lately, therefore need a new, more professional look.
We are a modern, non-stuffy chiropractic office.  Want a contemporary look that will let people know this is not your typical doctors office.  Our logo is red, and contains the name of our business: realign.  The u in the logo is green, stressing the most important part of our business: "u"

Target Market(s)
moderate to upper income bracket, family friendly
www.realignspine-example.com
Gordon Pell
Family Chiropractor
314 Hollis Rd
Bastrop, TX 78999
512.555.0147 phone
512.555.0148 fax
Industry/Entity Type
Business
Requirements
Must have
- www.realignspine-example.com
Gordon Pell
Family Chiropractor
314 Hollis Rd
Bastrop, TX 78999
512.555.0147 phone
512.555.0148 fax

```html
<!DOCTYPE html>
<html lang="en">
<head>
<meta charset="utf-8">
<title>realign – Business Card</title>
<link href="https://fonts.googleapis.com/css2?family=Questrial&family=Montserrat:wght@700;800&display=swap" rel="stylesheet">
<style>
  :root {
    --backdrop: #1c1c1c;
    --leaf: #6db544;
    --leaf-dark: #5aa332;
    --signal: #ef4136;
    --paper: #ffffff;
    --ink: #2b2b2b;
  }
  * { margin: 0; padding: 0; box-sizing: border-box; }
  html, body {
    width: 1200px; height: 900px; overflow: hidden;
    background: var(--backdrop);
  }
  .stage {
    position: relative; width: 1200px; height: 900px;
    display: flex; align-items: center; justify-content: center; gap: 40px;
  }
  .card {
    position: relative; width: 540px; height: 310px;
    border-radius: 26px; overflow: hidden;
    box-shadow: 0 14px 30px rgba(0,0,0,.55);
  }
  /* Front */
  .card--front { background: var(--leaf); }
  .front-name {
    position: absolute; left: 0; right: 0; top: 112px; text-align: center;
    font-family: "Questrial", sans-serif; font-size: 64px; letter-spacing: 2px;
    color: var(--paper);
  }
  .front-tab {
    position: absolute; right: 0; bottom: 0; width: 290px; height: 40px;
    background: var(--paper); border-top-left-radius: 10px;
    display: flex; align-items: center; justify-content: center;
    font-family: "Questrial", sans-serif; font-size: 15px; color: var(--signal);
  }
  /* Back */
  .card--back { background: var(--paper); }
  .back-art { position: absolute; inset: 0; }
  .back-name {
    position: absolute; left: 44px; top: 52px;
    font-family: "Questrial", sans-serif; font-size: 50px; letter-spacing: 1px;
    color: var(--signal);
  }
  .contact {
    position: absolute; left: 338px; top: 40px; list-style: none;
    font-family: "Questrial", sans-serif; font-size: 14px; color: var(--ink);
  }
  .contact li { display: flex; align-items: flex-start; gap: 8px; margin-bottom: 7px; line-height: 1.35; }
  .contact svg { flex: none; margin-top: 1px; }
  .person { position: absolute; left: 30px; top: 196px; }
  .person-name {
    font-family: "Montserrat", sans-serif; font-weight: 800; font-size: 24px; color: var(--signal);
  }
  .person-role {
    font-family: "Montserrat", sans-serif; font-weight: 700; font-size: 15px; color: var(--leaf-dark);
  }
</style>
</head>
<body>
<main class="stage">
  <section class="card card--front" aria-label="Card front">
    <div class="front-name">realign</div>
    <div class="front-tab">www.realignspine-example.com</div>
  </section>

  <section class="card card--back" aria-label="Card back">
    <svg class="back-art" width="540" height="310" viewBox="0 0 540 310" aria-hidden="true">
      <defs>
        <linearGradient id="accent-fade" x1="0" y1="0" x2="1" y2="0">
          <stop offset="0" stop-color="#ef4136" stop-opacity="0"/>
          <stop offset="1" stop-color="#ef4136"/>
        </linearGradient>
      </defs>
      <polygon points="0,312 540,176 540,310 0,310" fill="#ef4136"/>
      <line x1="0" y1="300" x2="540" y2="164" stroke="#6db544" stroke-width="3"/>
      <line x1="150" y1="140" x2="235" y2="150" stroke="url(#accent-fade)" stroke-width="3"/>
      <text x="290" y="274" transform="rotate(-14 290 274)" font-family="Questrial, sans-serif" font-size="15" fill="#ffffff">www.realignspine-example.com</text>
    </svg>

    <div class="back-name">realign</div>

    <ul class="contact">
      <li>
        <svg width="18" height="18" viewBox="0 0 18 18"><circle cx="9" cy="9" r="8" fill="#fff" stroke="#ef4136" stroke-width="1.6"/><path d="M4.5 9 9 5l4.5 4h-1.4v4H10v-2.5H8V13H5.9V9z" fill="#6db544"/></svg>
        <span>314 Hollis Rd<br>Bastrop, TX 78999</span>
      </li>
      <li>
        <svg width="18" height="18" viewBox="0 0 18 18"><circle cx="9" cy="9" r="8" fill="#fff" stroke="#ef4136" stroke-width="1.6"/><path d="M6 5c.6-.4 1.2 0 1.5.6l.6 1.3c.2.5 0 .9-.4 1.2l-.4.3c.5 1.1 1.3 1.9 2.4 2.4l.3-.4c.3-.4.7-.6 1.2-.4l1.3.6c.6.3 1 .9.6 1.5-.6 1-1.6 1.2-2.6.8C8.3 12 6 9.7 5.1 7.6c-.4-1-.2-2 .9-2.6z" fill="#6db544"/></svg>
        <span>512.555.0147</span>
      </li>
      <li>
        <svg width="18" height="18" viewBox="0 0 18 18"><circle cx="9" cy="9" r="8" fill="#fff" stroke="#ef4136" stroke-width="1.6"/><rect x="5.5" y="5" width="7" height="8" rx="1" fill="#6db544"/><rect x="7" y="7" width="4" height="1" fill="#fff"/><rect x="7" y="9" width="4" height="1" fill="#fff"/></svg>
        <span>512.555.0148</span>
      </li>
    </ul>

    <div class="person">
      <div class="person-name">Gordon Pell</div>
      <div class="person-role">Family Chiropractor</div>
    </div>
  </section>
</main>
</body>
</html>
```